PowerPoint Design TELM

I have now selected the logo for my consultancy company. I need some innovative design for my Powerpoint slides. The audience is senior executives in international banks predominantly in Asia, but also in the Middle East, Africa and Latin America.
My company advises them on solutions to be able to grow their business.
This is my main means of hooking the clients and it is crucial to the success of my business.
I will update the file to a vector file in a few hours.

I am looking for a complete template.

Senior hard nosed executives in international Banks

```html
<!DOCTYPE html>
<html lang="en">
<head>
<meta charset="utf-8">
<title>Several charts + text slide</title>
<link rel="stylesheet" href="https://fonts.googleapis.com/css2?family=Carlito:wght@400;700&family=Cabin:wght@400&display=swap">
<style>
  :root {
    --teal: #78cdd0;
    --teal-dark: #5fbcc0;
    --yellow: #e4e625;
    --lime: #c6de4c;
    --ink: #222222;
    --body-text: #767676;
    --bg-top: #ededed;
    --bg-bottom: #e4e4e4;
    --white: #ffffff;
  }
  * { margin: 0; padding: 0; box-sizing: border-box; }
  html, body { width: 1200px; height: 900px; overflow: hidden; }
  body {
    position: relative;
    background: radial-gradient(ellipse at 80% 40%, #f9f9f9 0%, var(--bg-top) 55%, var(--bg-bottom) 100%);
    font-family: "Carlito", "Calibri", sans-serif;
  }
  .slide-header {
    position: absolute; left: 0; top: 0;
    width: 1200px; height: 150px;
    background: var(--teal);
    box-shadow: 0 3px 6px rgba(0,0,0,0.25);
  }
  .slide-title {
    position: absolute; left: 36px; top: 44px;
    color: var(--white);
    font-size: 52px; font-weight: 400;
    letter-spacing: 0.2px;
  }
  .panel {
    position: absolute;
    border: 1.5px dashed var(--teal);
  }
  .panel--line { left: 42px; top: 176px; width: 577px; height: 334px; }
  .panel--bar  { left: 42px; top: 529px; width: 577px; height: 340px; }
  .panel--text { left: 637px; top: 176px; width: 530px; height: 604px; }
  .chart { position: absolute; left: 0; top: 0; }
  .chart text { font-family: "Carlito", "Calibri", sans-serif; font-size: 18px; fill: var(--ink); }
  .bullet-list {
    list-style: none;
    position: absolute; left: 55px; top: 20px; width: 430px;
    font-family: "Cabin", "Gill Sans", sans-serif;
    font-size: 18.5px; line-height: 38px;
    color: var(--body-text);
  }
  .bullet-list li { position: relative; padding-left: 37px; margin-bottom: 10px; }
  .bullet-list li::before {
    content: "–"; position: absolute; left: 0; top: 0;
    color: var(--lime);
  }
  .brand {
    position: absolute; left: 1030px; top: 812px;
    display: flex; align-items: center; gap: 12px;
    font-family: "Cabin", "Gill Sans", sans-serif;
    font-size: 26px; color: #6f6f6f;
  }
  .brand-mark { width: 60px; height: 60px; border-radius: 50%; background: var(--teal); }
</style>
</head>
<body>
  <header class="slide-header">
    <h1 class="slide-title">Several charts + text slide</h1>
  </header>

  <section class="panel panel--line"></section>
  <svg class="chart line-chart" width="1200" height="900" viewBox="0 0 1200 900" aria-label="Line chart of series A, B and C, 2010 to 2013">
    <g stroke="#8a8a8a" stroke-width="1.2">
      <line x1="131" y1="200" x2="131" y2="460"/>
      <line x1="131" y1="460" x2="495" y2="460"/>
    </g>
    <g text-anchor="end">
      <text x="112" y="206">6</text><text x="112" y="249">5</text>
      <text x="112" y="293">4</text><text x="112" y="336">3</text>
      <text x="112" y="379">2</text><text x="112" y="423">1</text>
      <text x="112" y="466">0</text>
    </g>
    <g text-anchor="middle">
      <text x="176" y="494">2010</text><text x="267" y="494">2011</text>
      <text x="358" y="494">2012</text><text x="449" y="494">2013</text>
    </g>
    <g fill="none" stroke-width="3.5" stroke-linejoin="round">
      <polyline stroke="var(--teal)" points="176,274 267,352 358,308 449,265"/>
      <polyline stroke="var(--yellow)" points="176,356 267,269 358,382 449,339"/>
      <polyline stroke="var(--lime)" points="176,373 267,373 358,330 449,243"/>
    </g>
    <g fill="var(--teal)">
      <rect x="171" y="269" width="10" height="10" transform="rotate(45 176 274)"/>
      <rect x="262" y="347" width="10" height="10" transform="rotate(45 267 352)"/>
      <rect x="353" y="303" width="10" height="10" transform="rotate(45 358 308)"/>
      <rect x="444" y="260" width="10" height="10" transform="rotate(45 449 265)"/>
    </g>
    <g fill="var(--yellow)">
      <rect x="170" y="350" width="12" height="12"/><rect x="261" y="263" width="12" height="12"/>
      <rect x="352" y="376" width="12" height="12"/><rect x="443" y="333" width="12" height="12"/>
    </g>
    <g fill="var(--lime)">
      <polygon points="176,366 183,378 169,378"/><polygon points="267,366 274,378 260,378"/>
      <polygon points="358,323 365,335 351,335"/><polygon points="449,236 456,248 442,248"/>
    </g>
    <g stroke-width="3.5">
      <line x1="518" y1="310" x2="548" y2="310" stroke="var(--teal)"/>
      <line x1="518" y1="344" x2="548" y2="344" stroke="var(--yellow)"/>
      <line x1="518" y1="379" x2="548" y2="379" stroke="var(--lime)"/>
    </g>
    <rect x="528" y="305" width="10" height="10" fill="var(--teal)" transform="rotate(45 533 310)"/>
    <rect x="527" y="338" width="12" height="12" fill="var(--yellow)"/>
    <polygon points="533,372 540,384 526,384" fill="var(--lime)"/>
    <text x="555" y="316">A</text><text x="555" y="350">B</text><text x="555" y="385">C</text>
  </svg>

  <section class="panel panel--bar"></section>
  <svg class="chart bar-chart" width="1200" height="900" viewBox="0 0 1200 900" aria-label="Bar chart of series A, B and C, 2010 to 2013">
    <g stroke="#8a8a8a" stroke-width="1.2">
      <line x1="124" y1="548" x2="124" y2="810"/>
      <line x1="124" y1="810" x2="469" y2="810"/>
    </g>
    <g text-anchor="end">
      <text x="108" y="587">2013</text><text x="108" y="652">2012</text>
      <text x="108" y="718">2011</text><text x="108" y="783">2010</text>
    </g>
    <g text-anchor="middle">
      <text x="124" y="843">0</text><text x="239" y="843">2</text>
      <text x="354" y="843">4</text><text x="469" y="843">6</text>
    </g>
    <g fill="var(--lime)">
      <rect x="125" y="559" width="287" height="14"/><rect x="125" y="625" width="172" height="14"/>
      <rect x="125" y="690" width="115" height="14"/><rect x="125" y="756" width="115" height="14"/>
    </g>
    <g fill="var(--yellow)">
      <rect x="125" y="573" width="161" height="14"/><rect x="125" y="639" width="104" height="14"/>
      <rect x="125" y="704" width="253" height="15"/><rect x="125" y="770" width="138" height="15"/>
    </g>
    <g fill="var(--teal)">
      <rect x="125" y="587" width="259" height="15"/><rect x="125" y="653" width="201" height="15"/>
      <rect x="125" y="719" width="143" height="15"/><rect x="125" y="785" width="247" height="15"/>
    </g>
    <rect x="501" y="654" width="11" height="11" fill="var(--lime)"/>
    <rect x="501" y="687" width="11" height="11" fill="var(--yellow)"/>
    <rect x="501" y="721" width="11" height="11" fill="var(--teal)"/>
    <text x="518" y="666">C</text><text x="518" y="699">B</text><text x="518" y="733">A</text>
  </svg>

  <section class="panel panel--text">
    <ul class="bullet-list">
      <li>Lorem ipsum dolor sit amet, consectetur adipiscing elit. Proin in velit facilisis libero consectetur adipiscing.</li>
      <li>Aenean congue euismod erat, eu adipiscing dui gravida in.</li>
      <li>Donec vehicula tellus sit amet est aliquam ac pretium lacus aliquam.</li>
      <li>Suspendisse potenti. Integer est nunc, dignissim ac sagittis sit amet, pretium sit amet libero.</li>
      <li>Cras id nibh et ipsum ultrices pretium. Curabitur id leo tellus, a convallis justo. In turpis magna, aliquam ut consequat et, tempor ultrices mauris.</li>
    </ul>
  </section>

  <div class="brand">
    <span class="brand-mark"></span>
    <span class="brand-name">TELM</span>
  </div>
</body>
</html>
```